Business Card Design

Consultation for design, construction athletic facilities specializing in synthetic turf systems and all weather running track systems.
Motto "True Owner Representation"
New Company that we'd like to highlight the LOGO first and foremost with the colors of the background and font as primary colors of the card too if possible. I've also attached a typical larger project design layout that could be used in the background to highlight our design and construction specialty.
Website is something we want very noticeable for driving traffic.
Target Market(s)
Athletic Directors, Designers, Government and Military, Contractors
Industry/Entity Type
Construction
Contact Information for Business Card
Peter L. Vandrell CFB, CTB
48317 W 63rd Ave
Harlow Ridge, WA 99482
C +1 503.555.0147
O +1 808.555.0182
Peter@fieldlaneco.example
www.fieldlaneco.example

```html
<!DOCTYPE html>
<html lang="en">
<head>
<meta charset="utf-8">
<title>Corvane Sport – Business Card</title>
<link rel="stylesheet" href="https://fonts.googleapis.com/css2?family=Arimo:wght@400&display=swap">
<style>
  :root {
    --backdrop: #2b2b2b;
    --card: #000000;
    --copper: #d98a3a;
    --copper-soft: #c98a55;
    --rule: #b9834f;
  }
  html, body {
    margin: 0;
    padding: 0;
    width: 1200px;
    height: 800px;
    overflow: hidden;
    background: var(--backdrop);
  }
  .canvas {
    position: relative;
    width: 1200px;
    height: 800px;
    font-family: "Arimo", Arial, sans-serif;
  }
  .card {
    position: absolute;
    top: 249px;
    width: 504px;
    height: 287px;
    background: var(--card);
    box-shadow: 0 4px 14px rgba(0,0,0,0.55);
  }
  .card--front { left: 60px; }
  .card--back  { left: 628px; }
  .card svg { display: block; width: 504px; height: 287px; }
  .brand-square { fill: var(--copper); }
  .brand-name, .brand-sub, .tagline, .holder-name, .holder-title, .contact-text, .address {
    font-family: "Arimo", Arial, sans-serif;
    font-weight: 400;
    fill: var(--copper);
  }
  .brand-name { letter-spacing: 3px; }
  .brand-sub  { letter-spacing: 4px; }
  .holder-title, .contact-text, .address { fill: var(--copper-soft); }
  .divider { stroke: var(--rule); stroke-width: 1.2; }
  .icon { fill: none; stroke: var(--copper-soft); stroke-width: 1.3; }
  .icon-fill { fill: var(--copper-soft); }
</style>
</head>
<body>
<main class="canvas">

  <section class="card card--front" aria-label="Card front">
    <svg viewBox="0 0 504 287">
      <rect class="brand-square" x="140" y="117" width="14" height="14"/>
      <text class="brand-name" x="400" y="145" font-size="44" text-anchor="end">CORVANE</text>
      <text class="brand-sub" x="400" y="177" font-size="26" text-anchor="end">sport</text>
      <text class="tagline" x="402" y="220" font-size="16" text-anchor="end">True Owner Representation</text>
    </svg>
  </section>

  <section class="card card--back" aria-label="Card back">
    <svg viewBox="0 0 504 287">
      <rect class="brand-square" x="80" y="62" width="10" height="10"/>
      <text class="brand-name" x="264" y="81" font-size="30" text-anchor="end">CORVANE</text>
      <text class="brand-sub" x="264" y="104" font-size="18" text-anchor="end">sport</text>

      <text class="holder-name" x="480" y="157" font-size="21" text-anchor="end">Peter L. Vandrell</text>
      <line class="divider" x1="0" y1="170" x2="402" y2="170"/>
      <text class="holder-title" x="480" y="180" font-size="14" text-anchor="end">CFB, CTB</text>

      <g class="contact-list">
        <rect class="icon" x="37" y="194" width="8" height="12" rx="1.5"/>
        <text class="contact-text" x="52" y="205" font-size="13.6">+1 503.555.0147</text>
        <path class="icon-fill" d="M34 217 q7 -5 14 0 l-1 3 h-3 l-1 -2 h-4 l-1 2 h-3 z M36 221 h10 l1 5 h-12 z"/>
        <text class="contact-text" x="52" y="224" font-size="13.6">+1 808.555.0182</text>
        <rect class="icon" x="34" y="235" width="14" height="9"/>
        <path class="icon" d="M34 235 l7 5 l7 -5"/>
        <text class="contact-text" x="52" y="243" font-size="13.6">Peter@fieldlaneco.example</text>
        <circle class="icon-fill" cx="41" cy="258" r="7"/>
        <path d="M34 258 h14 M41 251 v14" stroke="#000" stroke-width="1"/>
        <text class="contact-text" x="52" y="262" font-size="13.6">www.fieldlaneco.example</text>
      </g>

      <text class="address" x="278" y="245" font-size="13.6">48317 W 63rd Ave Harlow Ridge,</text>
      <text class="address" x="278" y="263" font-size="13.6">WA 99482</text>
    </svg>
  </section>

</main>
</body>
</html>
```